Trellin Crates web design

I am after a web page design I can upload onto Wexmor Launch! - which assists in building an ebusiness. I wish the site to have a vintage feel with a modern approach. I am fond of scroll or floral type motifs. As the web site will focus on home storage solutions, I would also like a practical feel too. I have a logo designed and ready to upload.

Target Market(s)

My target market is mature homeowners, particularly women who want stylish solutions to home storage.

Industry/Entity Type

Building

Requirements
Must have
• Logo to be prominent with co-ordinating background design. Navbar buttons to the left with similar background panel. far right column left available for associated links and advertisements.

```html
<!DOCTYPE html>
<html lang="en">
<head>
<meta charset="utf-8">
<title>Trellin Crates — Home Storage</title>
<link href="https://fonts.googleapis.com/css2?family=Arimo:wght@400;700&family=Tinos&family=Questrial&display=swap" rel="stylesheet">
<style>
:root{
  --page:#ece5db;
  --page-deep:#d9cbb8;
  --brown:#9b6d4b;
  --brown-dark:#7d5536;
  --brown-light:#b88b66;
  --heading:#8a5a34;
  --ink:#222;
  --muted:#555;
  --panel:#fff;
  --line:#e3ddd5;
  --ad:#a98362;
}
*{box-sizing:border-box;margin:0;padding:0}
html,body{width:1200px;height:978px;overflow:hidden}
body{position:relative;background:var(--page);font-family:"Arimo",Arial,sans-serif;color:var(--ink)}
.backdrop{position:absolute;inset:0;background:radial-gradient(ellipse at 15% 20%,#e2d6c6 0,transparent 45%),radial-gradient(ellipse at 90% 80%,#ddd0bd 0,transparent 50%),linear-gradient(135deg,#efe9e0,#e3d8c9)}
.abs{position:absolute}
.logo{left:194px;top:26px;display:flex;align-items:center;gap:10px;font-size:28px;font-weight:700;color:#4f4f55}
.logo-dot{width:30px;height:30px;border-radius:50%;background:#4f4f55}
.navbar{left:180px;top:85px;width:840px;height:36px;border-radius:4px;background:linear-gradient(#b2896a,var(--brown) 55%,var(--brown-dark));display:flex;align-items:center;padding:0 16px;box-shadow:0 1px 2px rgba(0,0,0,.2)}
.nav-links{display:flex;list-style:none;font-family:"Tinos",serif;font-size:13px;color:#fff;letter-spacing:.3px}
.nav-links li+li::before{content:"|";margin:0 10px;opacity:.8}
.follow{margin-left:auto;display:flex;align-items:center;gap:7px;font-size:10px;font-weight:700;color:#fff}
.follow span.sq{width:22px;height:22px;border-radius:3px;background:#eee7de}
.flourish{top:180px;width:26px;height:170px;background:linear-gradient(#c5a183,#9f7453);border-radius:13px;opacity:.7}
.banner{left:180px;top:132px;width:840px;height:274px;border:3px solid #fff;border-radius:6px;overflow:hidden;box-shadow:0 1px 4px rgba(0,0,0,.2);background:linear-gradient(90deg,#a8a49f,#c9c6c1 45%,#bdbab4)}
.banner-scene{position:absolute;right:30px;top:20px;width:470px;height:230px;background:linear-gradient(#bdb9b3 0,#c3bfb8 50%,#5a3a2c 52%,#4a2e22 72%,#d6d3cd 74%,#c8c5bf);border-radius:4px;opacity:.9}
.banner-copy{position:absolute;left:32px;top:22px;color:#fff;font-family:"Questrial",sans-serif}
.banner-copy h1{font-weight:400;font-size:54px;line-height:50px}
.banner-copy p{margin-top:28px;font-size:17px;line-height:20px;color:#3d3a37}
.banner-copy b{font-family:"Arimo",sans-serif;font-size:14px}
.panel{background:var(--panel);border-radius:4px;box-shadow:0 1px 3px rgba(0,0,0,.2)}
.panel h2{font-size:14px;font-weight:700;color:var(--heading)}
.search{left:182px;top:422px;width:197px;height:82px;padding:12px 17px}
.field{margin-top:14px;height:24px;border-radius:12px;background:#eceae7;border:1px solid #dcd8d3;display:flex;align-items:center;justify-content:space-between;padding-left:10px;font-size:10px;color:#999}
.field .go{width:28px;height:22px;border-radius:11px;background:#fff;display:flex;align-items:center;justify-content:center}
.categories{left:182px;top:527px;width:197px;height:260px;list-style:none;padding-top:2px;font-family:"Tinos",serif;font-size:13px;color:#222}
.categories li{height:28.5px;line-height:28.5px;padding-left:22px;border-bottom:1px solid var(--line)}
.categories li:last-child{border:0}
.categories .current{background:#f6f2ee;position:relative}
.categories .current::before{content:"\203A";position:absolute;left:8px;color:var(--brown);font-weight:700}
.mailing{left:182px;top:804px;width:197px;height:97px;padding:10px 12px}
.mailing .field{margin-top:8px;color:#666;font-size:10px}
.btn-submit{position:absolute;right:10px;bottom:8px;width:56px;height:22px;border-radius:3px;background:linear-gradient(#f4f2ef,#d9d5cf);border:1px solid #c9c3bb;font-size:11px;font-weight:700;color:var(--brown-dark);text-align:center;line-height:20px}
.featured{left:397px;top:422px;width:407px;height:479px;padding:12px 14px}
.product{position:absolute;width:120px;text-align:center;font-size:11px}
.product .shot{width:100px;height:100px;margin:0 auto;border-radius:4px;background:linear-gradient(#e6e6e4,#b9b7b3)}
.product .name{margin-top:20px}
.product .price{font-weight:700;margin-top:3px}
.product .add{margin:7px auto 0;width:100px;height:22px;border-radius:3px;background:linear-gradient(var(--brown-light),var(--brown-dark));color:#fff;line-height:22px;font-size:11px}
.paging{position:absolute;left:16px;right:16px;bottom:14px;display:flex;justify-content:space-between;font-size:10px;font-weight:700;color:var(--muted)}
.cart{left:822px;top:422px;width:197px;height:82px;padding:10px 14px}
.cart p{margin-top:8px;font-size:11px;line-height:16px}
.ads{left:822px;top:521px;width:197px;height:381px;padding:9px}
.ad{height:178px;background:var(--ad);color:#fff;display:flex;flex-direction:column;align-items:center;justify-content:center;text-align:center}
.ad+.ad{margin-top:8px}
.ad .size{font-size:22px}
.ad .label{margin-top:38px;font-size:14px;font-weight:700;line-height:16px}
.footer{left:187px;top:928px;width:828px;display:flex;justify-content:space-between;font-size:11px}
.footer ul{display:flex;list-style:none}
.footer li+li::before{content:"|";margin:0 6px;color:#888}
</style>
</head>
<body>
<div class="backdrop" role="img" aria-label="Faint cream floral scroll pattern background"></div>

<div class="abs logo"><span class="logo-dot"></span>Trellin Crates</div>

<nav class="abs navbar">
  <ul class="nav-links">
    <li>HOME PAGE</li><li>NEW PRODUCTS</li><li>SPECIALS</li><li>ALL PRODUCTS</li><li>CONTACT US</li><li>FAQS</li>
  </ul>
  <div class="follow">FOLLOW US: <span class="sq"></span><span class="sq"></span></div>
</nav>

<div class="abs flourish" style="left:143px" role="img" aria-label="Brown scroll ornament"></div>
<div class="abs flourish" style="left:1031px" role="img" aria-label="Brown scroll ornament"></div>

<section class="abs banner">
  <div class="banner-scene" role="img" aria-label="Modern dark wood bed with side tables and lamp in a grey room"></div>
  <div class="banner-copy">
    <h1>Get<br>Organized<br>for Spring!</h1>
    <p>trellincrates has everything you need to<br>start your spring off on the right foot <b>Read More</b></p>
  </div>
</section>

<section class="abs panel search">
  <h2>Product Search</h2>
  <div class="field">Search Our Products
    <span class="go"><svg width="13" height="13" viewBox="0 0 13 13"><circle cx="5.5" cy="5.5" r="4" fill="none" stroke="#333" stroke-width="1.8"/><line x1="8.5" y1="8.5" x2="12" y2="12" stroke="#333" stroke-width="2"/></svg></span>
  </div>
</section>

<ul class="abs panel categories">
  <li class="current">FEATURED PRODUCTS</li><li>SPECIALS</li><li>BEDROOM</li><li>FAMILY ROOM</li><li>GARAGE</li><li>HOME OFFICE</li><li>KITCHEN</li><li>LAUNDRY</li><li>UTILITY</li>
</ul>

<section class="abs panel mailing">
  <h2>Join Our Mailing List</h2>
  <div class="field">Enter Your Email</div>
  <div class="btn-submit">Submit</div>
</section>

<section class="abs panel featured">
  <h2>FEATURED PRODUCTS</h2>
  <div class="product" style="left:6px;top:40px"><div class="shot" role="img" aria-label="Mesh stacking shelves"></div><div class="name">Mesh Stacking Selves</div><div class="price">$119.00</div><div class="add">Add to Cart</div></div>
  <div class="product" style="left:143px;top:40px"><div class="shot" role="img" aria-label="Cotton garment bags"></div><div class="name">Cotton Garment Bags</div><div class="price">$29.99</div><div class="add">Add to Cart</div></div>
  <div class="product" style="left:280px;top:40px"><div class="shot" role="img" aria-label="Rolling garment rack"></div><div class="name">Garment Rack</div><div class="price">$69.00</div><div class="add">Add to Cart</div></div>
  <div class="product" style="left:6px;top:224px"><div class="shot" role="img" aria-label="Grey underbed bag"></div><div class="name">Underbed Bag</div><div class="price">$14.99</div><div class="add">Add to Cart</div></div>
  <div class="product" style="left:143px;top:224px"><div class="shot" role="img" aria-label="Clear handbag organizer"></div><div class="name">Handbag Organizer</div><div class="price">$11.99</div><div class="add">Add to Cart</div></div>
  <div class="product" style="left:280px;top:224px"><div class="shot" role="img" aria-label="Fabric storage bins"></div><div class="name">Storage Bin</div><div class="price">$12.99</div><div class="add">Add to Cart</div></div>
  <div class="paging"><span>Displaying 1 to 10 (of 20 products)</span><span>1 2 [ Next&gt;&gt;]</span></div>
</section>

<section class="abs panel cart">
  <h2>My Cart</h2>
  <p>You Currently have no items in your shopping cart</p>
</section>

<aside class="abs panel ads">
  <div class="ad"><span class="size">200x200</span><span class="label">Advertisment<br>Placeholder</span></div>
  <div class="ad"><span class="size">200x200</span><span class="label">Advertisment<br>Placeholder</span></div>
</aside>

<footer class="abs footer">
  <span>© 2011 Trellin Crates. All Rights Reserved.</span>
  <ul><li>Bedroom</li><li>Family Room</li><li>Garage</li><li>Home Office</li><li>Kitchen</li><li>Laundry</li><li>Utility</li></ul>
</footer>
</body>
</html>
```